Systems and Technology Consultants - Website

Design & Build a website for a new company which operates in the Systems and Technology space for Transportation, Government and Commercial sectors.

Overall design should be minimalist in nature.
Should also have a feed that provides news and event updates on the main page.
Logo has already been awarded and should be incorporated into the site.

We like the overall layout, functionality and simplicity of the below sites. Submitted designs could be similar to or a combination of the aspects on these sites, or perhaps a whole different concept - we are open to new ideas.
Vortrane.com
Merp.it

Update 1 Dated 27 May 2014

All I am moving away from the Merp.it website and would like it to be more aligned with Vortrane.com not only in layout but in functionality. I will be extending the deadline of this design brief for two weeks to incorporate additional requirements and will add addtional funding to the project.

Apologies for not having more information available to provide but with so many submissions its getting confusing.

Thanks Dermot
Updates

Please note that the brief has been updated and the deadline has been extended.

Important: We will need two language versions of the website, English and Arabic; the website is hosted on HostPeak

Hello All, Thank you for your submissions. We have narrowed it down to the final 6 designers and I just wanted to take a moment and provide a bit of feedback regarding the concepts that we like and the modifications we are looking for. First, let me mention some of the design functions we like. - At the top of the homepage we really like the "region" or "language" tab so that the website can be viewed in both English and Arabic. - We like the homepage to have clear color variation so that the different sections of the homepage are distinct. Additionally, we like the bottom portion of the homepage to be in red. We feel that draws attention to our contact information. Again, we would like the colors to integrate black, gray-scale, red, etc. - Having a search tab at the top of the home page, or integrated into the main image, so that the site is easy to navigate. - We especially like the main image to have the scrolling tabs at the bottom so it is easy to browse the services offered (Consultancy, Solutions Architecture, Masters Systems Integration, Independent Design Review). - In regards to the services offered tab we really like the idea that a few people presented that have the outside of our logo with an icon in the middle of consultancy, solutions, etc., etc. Secondly, as mentioned in our brief we really enjoy the design of vortrane site. Specially, we enjoy the strong iconic images they use, the way the tabs at the top scroll easily, and contact us page that generates an email. Lastly, I've included some photos of the concept we have been working on. What we are trying to demonstrate is how our company offers a range of services that are essentially linked together. We provide individual services that when combined present the full service package. We would like this concept to be integrated into the over concept of our website. Please feel free to ask for clarification of any of the above points or contact us if you have any additional questions. We appreciate all of your hard work and are very excited to see the updated designs. Best, Miriam Dowbrook Plenvaro Senior Program Manager miriam.dowbrook@plenvaro-mail.com

Industry/Entity Type

Government

Font styles to use
Serif
Sans Serif

Requirements
Must have
• Must work on/adapt to various/mobile devices (responsive)
Must be simple and straightforward
Colors should be in line/matching with logo
2 language versions: English and Arabic (no Thai)
Services should be the first group/row of items after/below the main image
Note: the website will be hosted by hostpeak
Nice to have
• Submit feedback form
What's New section
The banner at the bottom of the site should not be too large; we would like a narrow one more
It would be nice if the header/top banner (with Home, About, etc. tabs) could stay in place as you scroll down (like Vortrane and Chatterly)
We will likely only use one image with a Company slogan on the Home page rather than a carousel of images to rotate through
Should not have
• This is the existing website: http://www.plenvaro-example.org
We do not like the animation, the way the banner icons/titles bounce
Not simple enough, we don't like the functionality or how pages load so slowly
We do not like the logo centered - it should be at the left
The banner and its tabs should not be towards the right, we would like them to be centered, to go all the way across and to be below the logo

```html
<!DOCTYPE html>
<html lang="en">
<head>
<meta charset="utf-8">
<title>Plenvaro — System Knowledge Delivered</title>
<link href="https://fonts.googleapis.com/css2?family=Roboto:wght@300;400;500&display=swap" rel="stylesheet">
<style>
:root{
  --red:#e8232f;
  --red-soft:#f04a55;
  --ink:#222;
  --header:#2b2b2b;
  --grey-text:#666;
  --grey-mid:#8a8a8a;
  --band-light:#f2f2f2;
  --band-mid:#e4e4e4;
  --band-news:#f4f4f4;
  --line:#c8c8c8;
  --white:#fff;
}
*{box-sizing:border-box;margin:0;padding:0}
html,body{width:1200px;height:2237px;overflow:hidden}
body{position:relative;font-family:'Roboto',Arial,sans-serif;color:var(--ink);background:var(--band-light)}
.abs{position:absolute}

/* header */
.site-header{left:0;top:0;width:1200px;height:136px;background:var(--header);box-shadow:0 2px 6px rgba(0,0,0,.4);z-index:2}
.region-tab{left:1024px;top:0;width:103px;height:30px;background:#4a4a4a;color:#ccc;font-size:11px;text-align:center;line-height:30px}
.nav-link{top:80px;color:var(--white);font-size:15px;font-weight:500;letter-spacing:.3px;text-transform:uppercase}
.brand{left:500px;top:30px;width:200px;text-align:center}
.brand-mark{display:block;width:26px;height:26px;margin:0 auto 10px;background:var(--red)}
.brand-name{color:var(--red);font-size:20px;font-weight:400;letter-spacing:5px}

/* hero */
.hero{left:0;top:136px;width:1200px;height:471px;background:linear-gradient(100deg,#dfe6ec 0%,#c9d3dc 35%,#eef2f5 60%,#b7c1ca 100%)}
.hero-title{left:284px;top:332px;width:632px;height:114px;background:rgba(60,60,60,.82);text-align:center}
.hero-title .name{color:var(--red);font-size:58px;font-weight:400;line-height:64px;padding-top:6px;letter-spacing:1px}
.hero-title .slogan{color:var(--white);font-size:35px;font-weight:400;line-height:38px;letter-spacing:1px}

/* welcome */
.welcome{left:0;top:607px;width:1200px;height:475px;background:var(--band-light)}
.divider-line{height:1px;background:var(--line)}
.divider-mark{width:26px;height:26px;border:3px solid #9a9a9a}
.section-title{color:var(--red);font-size:32px;font-weight:300;text-transform:uppercase;text-align:center}
.welcome-text{left:150px;top:200px;width:900px;text-align:center;color:var(--grey-text);font-size:27px;font-weight:300;line-height:35px;text-transform:uppercase}

/* services */
.services{left:0;top:1082px;width:1200px;height:375px;background:var(--band-mid)}
.service{top:120px;width:180px;text-align:center}
.service svg{display:block;margin:0 auto;height:96px}
.service-label{margin-top:10px;font-size:17px;color:#444;text-transform:uppercase;letter-spacing:.5px}
.service.is-active .service-label{color:var(--red)}

/* news */
.news{left:0;top:1457px;width:1200px;height:550px;background:var(--band-news)}
.news-heading{color:var(--red);font-size:32px;font-weight:300;text-transform:uppercase}
.news-thumb{width:191px;height:131px}
.news-item-title{left:288px;width:450px;font-size:17px;font-weight:500;line-height:22px;text-transform:uppercase;color:var(--ink)}
.news-item-body{left:288px;width:446px;font-size:12.5px;line-height:25.5px;color:var(--grey-text)}
.news-item-body .more{color:var(--red)}
.news-rule{left:74px;width:658px;height:1px;background:#ccc}
.btn-read{left:74px;top:480px;width:132px;height:40px;background:#666;color:var(--white);font-size:16px;text-align:center;line-height:40px;border:1px solid #555}

/* feedback */
.feedback-card{left:794px;top:101px;width:333px;height:419px;background:var(--white);box-shadow:0 0 8px rgba(0,0,0,.12)}
.field-label{left:23px;font-size:13px;color:#444;text-transform:uppercase}
.field{left:23px;width:286px;height:32px;border:1px solid #ccc;background:var(--white)}
.btn-submit{left:176px;top:360px;width:133px;height:40px;background:var(--red);color:var(--white);font-size:16px;text-align:center;line-height:40px;text-transform:uppercase}

/* footer */
.site-footer{left:0;top:2007px;width:1200px;height:230px;background:linear-gradient(180deg,var(--red-soft),var(--red))}
.footer-col{top:38px}
.footer-heading{font-size:14px;color:var(--ink);text-transform:uppercase;margin-bottom:6px}
.footer-col ul{list-style:none}
.footer-col li{font-size:13px;color:var(--white);line-height:25px}
.contact-row{display:flex;align-items:center;gap:12px;font-size:13px;color:var(--white);line-height:20px;margin-top:12px}
.social-dot{display:inline-block;width:20px;height:20px;border-radius:50%;background:var(--white);margin-right:12px;vertical-align:middle}
.social li{line-height:32px}
.footer-brand{left:900px;top:40px;width:150px;text-align:center}
.footer-brand .brand-mark{width:22px;height:22px;background:var(--white);margin-bottom:10px}
.footer-brand .brand-name{color:var(--white);font-size:17px}
.copyright{left:916px;top:2161px;font-size:12px;color:var(--white)}
</style>
</head>
<body>

<header class="site-header abs">
  <div class="region-tab abs">Select Region</div>
  <nav>
    <span class="nav-link abs" style="left:74px">Home</span>
    <span class="nav-link abs" style="left:184px">Business Unit</span>
    <span class="nav-link abs" style="left:356px">Services</span>
    <div class="brand abs"><span class="brand-mark"></span><span class="brand-name">PLENVARO</span></div>
    <span class="nav-link abs" style="left:757px">About Us</span>
    <span class="nav-link abs" style="left:895px">Locations</span>
    <span class="nav-link abs" style="left:1040px">Contact Us</span>
  </nav>
</header>

<section class="hero abs" role="img" aria-label="Photo of a smiling businessman in a white shirt holding a tablet in a bright office with colleagues behind">
  <div class="hero-title abs" style="left:284px;top:196px">
    <div class="name">PLENVARO</div>
    <div class="slogan">SYSTEM KNOWLEDGE DELIVERED</div>
  </div>
</section>

<section class="welcome abs">
  <div class="divider-line abs" style="left:74px;top:72px;width:453px"></div>
  <div class="divider-line abs" style="left:673px;top:72px;width:453px"></div>
  <div class="divider-mark abs" style="left:587px;top:59px"></div>
  <h1 class="section-title abs" style="left:0;top:150px;width:1200px">Welcome to Plenvaro</h1>
  <p class="welcome-text abs">Plenvaro specializes in delivering quality professional services and technical projects that support larger business goals.</p>
  <div class="divider-line abs" style="left:74px;top:387px;width:453px"></div>
  <div class="divider-line abs" style="left:673px;top:387px;width:453px"></div>
  <div class="divider-mark abs" style="left:587px;top:374px"></div>
</section>

<section class="services abs">
  <h2 class="section-title abs" style="left:0;top:42px;width:1200px">Services We Offered</h2>

  <div class="service is-active abs" style="left:78px">
    <svg viewBox="0 0 100 90" width="110"><ellipse cx="56" cy="36" rx="40" ry="30" fill="#1c1c1c"/><path d="M26 54 L10 78 L40 62 Z" fill="#1c1c1c"/><circle cx="40" cy="36" r="6" fill="#fff"/><circle cx="56" cy="36" r="6" fill="#fff"/><circle cx="72" cy="36" r="6" fill="#fff"/></svg>
    <div class="service-label">Consulting</div>
  </div>

  <div class="service abs" style="left:295px">
    <svg viewBox="0 0 100 90" width="100"><rect x="16" y="12" width="12" height="70" fill="#777"/><path d="M28 40 H82 V70 H28 Z M40 50 V62 H66 V50 Z" fill="#777" fill-rule="evenodd"/><rect x="28" y="24" width="30" height="6" fill="#777"/></svg>
    <div class="service-label">Engineering</div>
  </div>

  <div class="service abs" style="left:511px">
    <svg viewBox="0 0 100 90" width="100"><path d="M44 6 H56 L76 80 H24 Z" fill="#666"/><rect x="34" y="34" width="32" height="8" fill="#e4e4e4"/><rect x="29" y="56" width="42" height="8" fill="#e4e4e4"/><rect x="18" y="80" width="64" height="6" fill="#666"/></svg>
    <div class="service-label">Construction</div>
  </div>

  <div class="service abs" style="left:728px">
    <svg viewBox="0 0 110 90" width="110"><circle cx="36" cy="52" r="24" fill="none" stroke="#666" stroke-width="12" stroke-dasharray="9 6"/><circle cx="36" cy="52" r="14" fill="none" stroke="#666" stroke-width="8"/><circle cx="80" cy="26" r="16" fill="none" stroke="#666" stroke-width="9" stroke-dasharray="7 5"/><circle cx="80" cy="26" r="8" fill="none" stroke="#666" stroke-width="6"/></svg>
    <div class="service-label">Operations</div>
  </div>

  <div class="service abs" style="left:944px">
    <svg viewBox="0 0 100 90" width="100"><path d="M22 12 L80 74 L72 82 L14 20 Z" fill="#555"/><path d="M80 10 L90 20 L40 72 L28 84 L18 74 L30 62 Z" fill="#666"/><circle cx="20" cy="14" r="10" fill="none" stroke="#555" stroke-width="6"/></svg>
    <div class="service-label">Maintenance</div>
  </div>
</section>

<section class="news abs">
  <h2 class="news-heading abs" style="left:74px;top:44px">What's New</h2>

  <article>
    <div class="news-thumb abs" style="left:74px;top:115px;background:linear-gradient(135deg,#555,#9a9a9a 55%,#3a3a3a)" role="img" aria-label="Photo of a hand touching glowing gears"></div>
    <h3 class="news-item-title abs" style="top:122px">Duis aliquam nibh a dui iaculis viverra id a velit. Vivamus egestas risus in magna varius..</h3>
    <p class="news-item-body abs" style="top:168px">Aenean a nibh eget turpis vehicula tempus ac sed massa. Vestibulum dolor nulla, ultrices ac tincidunt sed, laoreet non est. Suspendisse lobortis turpis in odio blandit ac interdum lorem euismod. Etiam risus massa, vulputate eu pellentesque et, consectetur a neque...<span class="more">Continue Reading</span></p>
  </article>

  <div class="news-rule abs" style="top:272px"></div>

  <article>
    <div class="news-thumb abs" style="left:74px;top:296px;background:linear-gradient(135deg,#2f4a3c,#7c9a80 50%,#c98a3a)" role="img" aria-label="Photo of network server cables"></div>
    <h3 class="news-item-title abs" style="top:303px">Duis aliquam nibh a dui iaculis viverra id a velit. Vivamus egestas risus in magna varius..</h3>
    <p class="news-item-body abs" style="top:349px">Aenean a nibh eget turpis vehicula tempus ac sed massa. Vestibulum dolor nulla, ultrices ac tincidunt sed, laoreet non est. Suspendisse lobortis turpis in odio blandit ac interdum lorem euismod. Etiam risus massa, vulputate eu pellentesque et, consectetur a neque...<span class="more">Continue Reading</span></p>
  </article>

  <div class="btn-read abs">READ ALL</div>

  <h2 class="news-heading abs" style="left:793px;top:44px">Feedback</h2>
  <form class="feedback-card abs">
    <label class="field-label abs" style="top:26px">Name</label>
    <div class="field abs" style="top:44px"></div>
    <label class="field-label abs" style="top:94px">Email Address</label>
    <div class="field abs" style="top:112px"></div>
    <label class="field-label abs" style="top:162px">Contact No.</label>
    <div class="field abs" style="top:179px"></div>
    <label class="field-label abs" style="top:230px">Message.</label>
    <div class="field abs" style="top:248px;height:97px"></div>
    <div class="btn-submit abs">Submit Now</div>
  </form>
</section>

<footer class="site-footer abs">
  <div class="footer-col abs" style="left:74px">
    <h4 class="footer-heading">Company</h4>
    <ul><li>Home</li><li>Business Units</li><li>Services</li><li>About Us</li><li>Locations</li><li>Contact Us</li></ul>
  </div>
  <div class="footer-col abs" style="left:265px">
    <h4 class="footer-heading">Services</h4>
    <ul><li>Consulting</li><li>Engineering</li><li>Construction</li><li>Operations</li><li>Maintenance</li></ul>
  </div>
  <div class="footer-col abs" style="left:436px">
    <h4 class="footer-heading">Contact Info</h4>
    <div style="font-size:13px;color:#fff">We want to hear from you:</div>
    <div class="contact-row">
      <svg width="18" height="14" viewBox="0 0 18 14"><path d="M1 4 Q9 -2 17 4 L14 6 L12 4 H6 L4 6 Z" fill="#fff"/><rect x="4" y="7" width="10" height="6" fill="#fff"/></svg>
      +(00)-02-555-0142-7
    </div>
    <div class="contact-row">
      <svg width="18" height="12" viewBox="0 0 18 12"><rect x="0.5" y="0.5" width="17" height="11" fill="none" stroke="#fff"/><path d="M1 1 L9 7 L17 1" fill="none" stroke="#fff"/></svg>
      info@plenvaro-example.org
    </div>
  </div>
  <div class="footer-col social abs" style="left:689px">
    <h4 class="footer-heading">Connect Us</h4>
    <ul style="margin-top:-4px">
      <li><span class="social-dot"></span>Chatterly</li>
      <li><span class="social-dot"></span>Chirpline</li>
      <li><span class="social-dot"></span>Linkfolio</li>
      <li><span class="social-dot"></span>Rss</li>
    </ul>
  </div>
  <div class="footer-brand abs"><span class="brand-mark"></span><span class="brand-name">PLENVARO</span></div>
</footer>
<div class="copyright abs">Copyright © 2014. All Right Reserved</div>

</body>
</html>
```